" ESCRITORIO DE SERVICO CONSULTIVO PROVIDO POR PROFISSIONAIS COM AMPLA EXPERIENCIA NO SETOR ELETRICO COM ATUACAO ACIMA DE 13 ANOS DE EXPERIENCIA. ATUMOS ATRAVES DO ENGAJAMENTO DE AGENTES A PARTIR DE CONSULTA DA NECESSIDADE E ELABORACAO DE PACOTE DE SERVICOS ALINHADO A EXPECTATIVA DO CLIENTE. SERVICOS PRINCIPAIS: GESTAO DE PLEITOS DE CONTRATOS DE GERACAO, TRANSMISSAO E DISTRIBUICAO DE ENERGIA GESTAO DE PROCESSOS DE AQUISICAO DE EQUIPAMENTOS E SERVICOS PARA EMPREENDIMENTOS DE GERACAO, TRANSMISSAO E DISTRIBUICAO DE ENERGIA OUTROS SERVICOS: PLANEJAMENTO E GESTAO DE EMPREENDIMENTOS DE GERACAO, TRANSMISSAO E DISTRIBUICAO DE ENERGIA "

```html
<!DOCTYPE html>
<html lang="pt-BR">
<head>
<meta charset="UTF-8">
<title>Meridia Consultoria – Papel timbrado</title>
<link rel="stylesheet" href="https://fonts.googleapis.com/css2?family=Montserrat:wght@600;700;800&family=Open+Sans:wght@400;600;700&display=swap">
<style>
  :root {
    --backdrop: #e4e5e7;
    --paper: #ffffff;
    --ink: #2b2f36;
    --ink-soft: #5d626b;
    --gold: #e3a81e;
    --band: #2f3540;
    --band-text: #e9ebee;
  }
  * { margin: 0; padding: 0; box-sizing: border-box; }
  html, body { width: 1200px; height: 1200px; overflow: hidden; }
  body {
    background: var(--backdrop);
    font-family: "Open Sans", sans-serif;
    color: var(--ink);
    position: relative;
  }
  .letterhead {
    position: absolute;
    left: 211px; top: 50px;
    width: 778px; height: 1100px;
    background: var(--paper);
    box-shadow: 0 6px 24px rgba(0,0,0,.12);
  }
  .recipient {
    position: absolute; left: 64px; top: 72px;
    font-size: 12px; line-height: 1.45; font-weight: 700;
  }
  .recipient .label { font-weight: 400; color: var(--ink-soft); }
  .brand {
    position: absolute; right: 64px; top: 70px;
    display: flex; align-items: center; gap: 14px;
  }
  .brand-mark { width: 38px; height: 38px; background: var(--gold); }
  .brand-name {
    font-family: "Montserrat", sans-serif; font-weight: 800;
    font-size: 26px; letter-spacing: 3px; color: var(--ink); line-height: 1.05;
  }
  .brand-name small { display: block; font-size: 11px; letter-spacing: 6px; }
  .reference {
    position: absolute; right: 64px; top: 180px;
    text-align: right; font-size: 11px; line-height: 1.6; color: var(--ink-soft);
  }
  .letter-body {
    position: absolute; left: 64px; right: 64px; top: 250px;
    font-size: 12.5px; line-height: 1.75; color: var(--ink-soft);
  }
  .letter-body p { margin-bottom: 16px; text-align: justify; }
  .closing {
    position: absolute; left: 64px; top: 770px;
    font-size: 12px; color: var(--ink-soft);
  }
  .signature-area {
    width: 130px; height: 54px; margin: 10px 0 6px;
    background: linear-gradient(90deg, #e6e7ea, #f4f4f5);
  }
  .closing .signer { font-weight: 700; color: var(--ink); }
  .footer-band {
    position: absolute; left: 0; right: 0; bottom: 0; height: 130px;
    background: var(--band); color: var(--band-text);
    display: flex; flex-direction: column; justify-content: center;
    padding: 0 64px; gap: 6px; font-size: 12px;
  }
  .footer-band .row { display: flex; align-items: center; gap: 10px; }
  .footer-band svg { width: 14px; height: 14px; fill: var(--gold); flex: none; }
</style>
</head>
<body>
  <main class="letterhead">
    <section class="recipient">
      <div class="label">Para</div>
      <div>Sr. Carlos Andrade</div>
      <div>Diretor Executivo</div>
      <div>Energia Norte S.A.</div>
      <div>Av. Central, 450</div>
      <div>São Paulo, SP 01000</div>
    </section>

    <header class="brand">
      <span class="brand-mark" aria-hidden="true"></span>
      <div class="brand-name">MERIDIA<small>CONSULTORIA</small></div>
    </header>

    <div class="reference">
      <div>Referência: 001/24</div>
      <div>20 de abril, 2024</div>
    </div>

    <article class="letter-body">
      <p>Prezado Sr. Andrade, agradecemos o contato e a oportunidade de apresentar nossos serviços de consultoria para o setor elétrico. Nossa equipe reúne profissionais com mais de treze anos de experiência em projetos de geração, transmissão e distribuição de energia.</p>
      <p>A partir da consulta inicial, elaboramos um pacote de serviços alinhado às suas expectativas, incluindo gestão de pleitos contratuais, apoio em processos de aquisição de equipamentos e acompanhamento técnico de empreendimentos em todas as suas etapas.</p>
      <p>Permanecemos à disposição para agendar uma reunião e detalhar a proposta, com cronograma, escopo e valores adequados à realidade do seu projeto.</p>
      <p>Certos de sua atenção, aguardamos seu retorno.</p>
    </article>

    <section class="closing">
      <div>Atenciosamente,</div>
      <div class="signature-area" role="img" aria-label="Assinatura manuscrita do signatário"></div>
      <div class="signer">Rafael Moura</div>
      <div>Diretor</div>
    </section>

    <footer class="footer-band">
      <div class="row">
        <svg viewBox="0 0 24 24" aria-hidden="true"><path d="M12 2a7 7 0 0 0-7 7c0 5 7 13 7 13s7-8 7-13a7 7 0 0 0-7-7zm0 9.5A2.5 2.5 0 1 1 12 6a2.5 2.5 0 0 1 0 5.5z"/></svg>
        <span>Rua das Palmeiras, 210 - Centro - Campinas - SP - 13010-100</span>
      </div>
      <div class="row">
        <svg viewBox="0 0 24 24" aria-hidden="true"><circle cx="12" cy="12" r="10"/></svg>
        <span>www.meridiaconsult.com.br</span>
      </div>
      <div class="row">
        <svg viewBox="0 0 24 24" aria-hidden="true"><path d="M6.6 10.8a15 15 0 0 0 6.6 6.6l2.2-2.2a1 1 0 0 1 1-.25 11.4 11.4 0 0 0 3.6.57 1 1 0 0 1 1 1V20a1 1 0 0 1-1 1A17 17 0 0 1 3 4a1 1 0 0 1 1-1h3.5a1 1 0 0 1 1 1c0 1.25.2 2.45.57 3.57a1 1 0 0 1-.25 1z"/></svg>
        <span>(19) 3456-7810 &nbsp;|&nbsp; contato@meridiaconsult.com.br</span>
      </div>
      <div class="row">
        <svg viewBox="0 0 24 24" aria-hidden="true"><rect x="3" y="3" width="18" height="18" rx="3"/></svg>
        <span>@meridiaconsult</span>
      </div>
    </footer>
  </main>
</body>
</html>
```